Corrabeen Holiday Village Flyer Project

Flyer required for a holiday caravan park. I have attached the current flyer for the park and would like to use the same layout. Please also alter the changes to the text that I have marked up. Until the additional uploads for the new images are ready, could you please just leave those as a blank square and the images can be inserted once I have them loaded.

Target Market(s)

Holiday makers

Industry/Entity Type

Tourism

Colors
3176b5
33a6d7
0393ce
fbee3e
fbed22
ffffff
faa54b

Requirements
Must have
• copy the attached flyer
• Would like a better title font for the front text - "Corrabeen Holiday Village", please make that a more playful holiday feel font
• Please use images 001 & 002 as the front cover images
• I have more images to load up which will be done 4/7.
Nice to have
• would like a better colour back ground to the flyer, maybe blue-ish and then alter the colour of the text accordingly
Should not have
• Please use the attached flyer copy as a template

```html
<!DOCTYPE html>
<html lang="en">
<head>
<meta charset="utf-8">
<title>Corrabeen Holiday Village – Trifold Flyer</title>
<link href="https://fonts.googleapis.com/css2?family=Fredoka:wght@600&family=Montserrat:ital,wght@0,400;0,600;0,700;1,600&display=swap" rel="stylesheet">
<style>
  :root{
    --blue-deep:#3176b5;
    --blue:#33a6d7;
    --blue-mid:#0393ce;
    --yellow:#fbee3e;
    --yellow-strong:#fbed22;
    --lime:#d3de1f;
    --white:#ffffff;
    --map-grey:#e6e9e6;
    --photo:#6fb3de;
    --page:#eef3f7;
  }
  *{box-sizing:border-box;margin:0;padding:0}
  html,body{width:1200px;height:800px;overflow:hidden;background:var(--page);font-family:"Montserrat",sans-serif}
  .flyer{position:absolute;left:45px;top:30px;width:1110px;height:740px;display:flex;box-shadow:0 10px 30px rgba(20,60,100,.18)}
  .panel{position:relative;width:370px;height:740px;overflow:hidden;background:linear-gradient(160deg,var(--blue) 0%,var(--blue-mid) 55%,var(--blue-deep) 100%);color:var(--white)}
  .panel + .panel{border-left:1px solid rgba(255,255,255,.12)}
  .panel-art{position:absolute;inset:0;width:370px;height:740px}

  .brand-name{font-family:"Fredoka",sans-serif;font-weight:600;color:var(--white);text-align:center;line-height:1}
  .brand-name span{display:block}
  .brand-name .lead{font-size:46px;letter-spacing:.01em}
  .brand-name .sub{font-size:21px;letter-spacing:.2em;text-transform:uppercase;margin-top:6px}

  /* inside panel */
  .intro{position:absolute;left:36px;top:336px;width:300px;font-size:12.5px;line-height:1.45}
  .activities{position:absolute;left:40px;top:455px;display:flex;gap:26px}
  .activities ul{list-style:none}
  .activities li{font-size:12.5px;font-weight:600;font-style:italic;color:var(--yellow);margin-bottom:9px;height:13px;display:flex;align-items:center;gap:10px}
  .activities li::before{content:"";width:7px;height:7px;background:var(--white);flex:none}
  .tagline{position:absolute;left:0;width:370px;top:662px;text-align:center;font-size:13px;font-weight:600;font-style:italic;line-height:1.3;color:var(--blue-deep)}

  /* back panel */
  .mid-brand{position:absolute;left:0;width:370px;top:285px}
  .contact{position:absolute;left:40px;width:290px;top:430px}
  .contact h2{font-family:"Fredoka",sans-serif;font-size:22px;font-weight:600;color:var(--yellow);text-align:center;letter-spacing:.03em}
  .contact .rule{display:block;margin:6px auto 18px}
  .contact ul{list-style:none}
  .contact li{display:flex;align-items:center;gap:12px;font-size:12px;margin-bottom:12px}
  .contact svg.icon{flex:none}

  /* front cover */
  .cover-brand{position:absolute;left:0;width:370px;top:425px}
  .cover-phone{position:absolute;left:0;width:370px;top:528px;display:flex;justify-content:center;align-items:center;gap:10px;font-size:19px;font-weight:700}
  .cover-web{position:absolute;left:0;width:370px;top:621px;text-align:center;font-size:15px;font-weight:700;color:var(--blue-deep)}
</style>
</head>
<body>
<main class="flyer">

  <section class="panel panel-location">
    <svg class="panel-art" viewBox="0 0 370 740">
      <path d="M0 0 H330 Q310 260 0 290 Z" fill="var(--lime)" aria-hidden="true"/>
      <path d="M0 0 H300 Q282 232 0 262 Z" fill="var(--map-grey)" role="img" aria-label="Street map showing the park location"/>
      <g fill="none" stroke="var(--white)" stroke-width="1.2" opacity=".8" aria-hidden="true">
        <path d="M0 298 Q330 270 345 0"/>
        <path d="M0 306 Q338 276 353 0"/>
        <path d="M0 314 Q346 282 361 0"/>
        <path d="M0 322 Q354 288 369 0"/>
      </g>
      <path d="M0 650 Q185 655 370 625 V690 Q185 712 0 712 Z" fill="var(--yellow)" aria-hidden="true"/>
    </svg>
    <p class="intro">We are the second turn to the left, after the bridge. Ideally located nestled between Seabreeze Beach and Estuary, 3mins south of the Corrabeen cut with all the associated water activities and 15mins from Portsea CBD. Boasting a range of activities such as</p>
    <div class="activities">
      <ul>
        <li>Summer Concerts</li>
        <li>Festivals</li>
        <li>Art Gallery</li>
        <li>Dolphins Tours</li>
        <li>Movie Theatres</li>
        <li>Superb Restaurants</li>
        <li>Night Clubs</li>
      </ul>
      <ul>
        <li>Harbour Markets</li>
        <li>Portsea</li>
        <li>Performing</li>
        <li>Arts Centre</li>
        <li>Wineries</li>
        <li>Wildlife parks</li>
        <li>Taverns</li>
      </ul>
    </div>
    <p class="tagline">Historical sites and many more<br>tourist attractions!</p>
  </section>

  <section class="panel panel-contact">
    <svg class="panel-art" viewBox="0 0 370 740" aria-hidden="true">
      <g fill="none" stroke="var(--white)" stroke-width="1.4" opacity=".85">
        <path d="M120 0 Q150 120 370 170"/>
        <path d="M135 0 Q162 112 370 158"/>
        <path d="M150 0 Q175 104 370 146"/>
        <path d="M165 0 Q188 96 370 134"/>
        <path d="M180 0 Q201 88 370 122"/>
        <path d="M195 0 Q214 80 370 110"/>
      </g>
    </svg>
    <div class="mid-brand brand-name"><span class="lead">Corrabeen</span><span class="sub">Holiday Village</span></div>
    <div class="contact">
      <h2>CONTACT US</h2>
      <svg class="rule" width="220" height="10" viewBox="0 0 220 10"><path d="M2 8 Q110 -2 218 4" fill="none" stroke="var(--white)" stroke-width="1.2"/></svg>
      <ul>
        <li><svg class="icon" width="12" height="12" viewBox="0 0 24 24"><path d="M6.6 10.8a15 15 0 0 0 6.6 6.6l2.2-2.2a1 1 0 0 1 1-.25 11.4 11.4 0 0 0 3.6.6 1 1 0 0 1 1 1V20a1 1 0 0 1-1 1A17 17 0 0 1 3 4a1 1 0 0 1 1-1h3.5a1 1 0 0 1 1 1c0 1.25.2 2.45.6 3.6a1 1 0 0 1-.25 1z" fill="var(--white)"/></svg>618 9555 0142</li>
        <li><svg class="icon" width="12" height="12" viewBox="0 0 24 24"><path d="M12 2a7 7 0 0 0-7 7c0 5.2 7 13 7 13s7-7.8 7-13a7 7 0 0 0-7-7zm0 9.5A2.5 2.5 0 1 1 12 6.5a2.5 2.5 0 0 1 0 5z" fill="var(--white)"/></svg>27 Shoreline Road Corrabeen 6200 WA</li>
        <li><svg class="icon" width="12" height="12" viewBox="0 0 24 24"><rect x="2" y="5" width="20" height="14" rx="1.5" fill="none" stroke="var(--white)" stroke-width="2"/><path d="M2 6l10 7 10-7" fill="none" stroke="var(--white)" stroke-width="2"/></svg>info@corrabeenholiday.com.au</li>
        <li><svg class="icon" width="12" height="12" viewBox="0 0 24 24"><circle cx="12" cy="12" r="9.5" fill="none" stroke="var(--white)" stroke-width="2"/><path d="M2.5 12h19M12 2.5c3 3 3 16 0 19M12 2.5c-3 3-3 16 0 19" fill="none" stroke="var(--white)" stroke-width="1.6"/></svg>www.corrabeenholiday.com.au</li>
      </ul>
    </div>
  </section>

  <section class="panel panel-cover">
    <svg class="panel-art" viewBox="0 0 370 740">
      <defs><clipPath id="cover-photo-clip"><circle cx="235" cy="120" r="200"/></clipPath></defs>
      <circle cx="225" cy="135" r="215" fill="var(--lime)" aria-hidden="true"/>
      <path d="M10 150 Q60 360 330 335" fill="none" stroke="var(--white)" stroke-width="3" opacity=".9" aria-hidden="true"/>
      <rect x="0" y="0" width="370" height="330" fill="var(--photo)" clip-path="url(#cover-photo-clip)" role="img" aria-label="Cover photo: holiday makers jumping off a boat into the estuary"/>
      <path d="M0 600 Q185 620 370 590 V650 Q185 680 0 660 Z" fill="var(--yellow)" aria-hidden="true"/>
    </svg>
    <div class="cover-brand brand-name"><span class="lead">Corrabeen</span><span class="sub">Holiday Village</span></div>
    <div class="cover-phone">
      <svg width="18" height="18" viewBox="0 0 24 24" aria-hidden="true"><path d="M6.6 10.8a15 15 0 0 0 6.6 6.6l2.2-2.2a1 1 0 0 1 1-.25 11.4 11.4 0 0 0 3.6.6 1 1 0 0 1 1 1V20a1 1 0 0 1-1 1A17 17 0 0 1 3 4a1 1 0 0 1 1-1h3.5a1 1 0 0 1 1 1c0 1.25.2 2.45.6 3.6a1 1 0 0 1-.25 1z" fill="var(--white)"/></svg>
      618 9555 0142
    </div>
    <p class="cover-web">www.corrabeenholiday.com.au</p>
  </section>

</main>
</body>
</html>
```